Website Redesign

We're looking for an artist with experience designing children's websites to redesign a children's video sharing website (like ClipNarvo, but for kids ages 4-14). It should be simple, uncluttered, and easy to use. To see our logo and current layout, go to www.Pebblopa.com. We've uploaded 2 possible layouts that include all elements except the RULES button, but we aren't artists and these might not be the most user-friendly layouts for kids. We've also listed links to some other video-sharing & kids' websites in the target customer section below.
Updates
Thank you for submitting your designs for our website project. We're reviewing all the designs now, and we may contact you to request a slight modification for the home page or for back pages.
Target Market(s)
Kids ages 4-14 who go online to upload & watch videos & images, play games, enter contests, and network. Here are links to some other video-sharing or childrens' websites:
http://wemlorafun.com
http://pavo.com
http://harborotter.com
http://clipnarvo.com
http://tlvjunior.org/
http://marlowe.go.com/index
http://kids.meridianatlasworld.com/kids/
http://www.hiddenmasonry.com
http://www.tots578.com/home.php
Industry/Entity Type
Artists
Requirements
Must have
- Kid-friendly design (easy to use, friendly feel).
Visually simple.
Must include these elements:
-Logo
-Search Bar
-Video Announcement player (see current site, but can be smaller)
-Text Announcement area (can be scrolling)
-Video Categories
-3 Ads (Banner or Video)
-Recent Tags
-Thumbnails of Featured Videos
-Buttons: LOG IN, SIGN UP, UPLOAD, PARENTS, CONTESTS, VIDEOS, IMAGES, GAMES, BLOGS, STORE, RULES.
Nice to have
- We like the rounded look of the buttons on our current site, but let us know if you have another idea.
Should not have
- The design should be for children, but NOT childish because the members range in age from 4-14. The design should have little or no illustrations to clutter the page because we don't want to distract from the content.

```html
<!DOCTYPE html>
<html lang="en">
<head>
<meta charset="utf-8">
<title>Pebblopa</title>
<link href="https://fonts.googleapis.com/css2?family=Kavivanar&display=swap" rel="stylesheet">
<style>
:root{
  --sky:#3badde;
  --panel:#4176ea;
  --ink:#151515;
  --gold:#f1bf00;
  --gold-edge:#2a2a2a;
  --text-light:#ffffff;
  --bullet:#c0393b;
  --bullet-rim:#e8e8e8;
  --scroll-track:#333333;
}
*{box-sizing:border-box;margin:0;padding:0}
html,body{width:750px;height:1200px;overflow:hidden}
body{background:var(--sky);font-family:"Kavivanar",cursive;color:var(--text-light);position:relative;letter-spacing:1px}
.abs{position:absolute}
.btn{position:absolute;height:34px;border-radius:17px;background:var(--gold);border:3px solid var(--gold-edge);box-shadow:2px 3px 0 var(--gold-edge);color:#fff;font-size:18px;display:flex;align-items:center;justify-content:center;letter-spacing:1.5px;white-space:nowrap}
.panel{position:absolute;background:var(--panel);border:3px solid var(--ink);border-radius:10px}
.brand{left:36px;top:62px;width:160px;display:flex;align-items:center;gap:8px;font-size:30px;color:#fff;letter-spacing:0}
.brand-mark{width:18px;height:18px;background:var(--gold);border-radius:50%}
.search-field{left:208px;top:83px;width:194px;height:28px;background:#fff;border:2px solid var(--ink);border-radius:14px}
.media{position:absolute;border:3px solid var(--ink);border-radius:10px;overflow:hidden}
.play{position:absolute;left:50%;top:50%;transform:translate(-50%,-50%)}
.announce{overflow:hidden}
.announce ul{list-style:none;margin-top:-7px;padding-left:16px}
.announce li{display:flex;align-items:center;gap:20px;height:40.5px;font-size:14px}
.bullet{flex:none;width:22px;height:22px;background:var(--bullet);border:3px solid var(--bullet-rim);border-radius:4px}
.scroll{position:absolute;left:266px;top:2px;width:12px;height:148px;background:var(--scroll-track);border-radius:4px;overflow:hidden}
.scroll span{display:block;height:112px;background:var(--gold)}
.cat-list{list-style:none;padding:18px 2px 0 4px}
.cat-list li{display:flex;justify-content:space-between;font-size:14.5px;line-height:22.6px;white-space:nowrap}
.thumb{position:absolute;width:80px;height:72px;border:1px solid var(--ink)}
.thumb-girl{background:radial-gradient(circle at 50% 55%,#c9a58e 0 22%,transparent 40%),linear-gradient(180deg,#3e3a36,#6d625a)}
.thumb-title{background:linear-gradient(180deg,#9dbbd0 0%,#8fbfa4 55%,#4f9a66 100%)}
.thumb-pet{background:radial-gradient(circle at 45% 45%,#9a6a45 0 26%,transparent 42%),linear-gradient(180deg,#d56e8e,#2b5fb0)}
.thumb-boy{background:radial-gradient(circle at 50% 50%,#d3ad96 0 26%,transparent 44%),linear-gradient(135deg,#5d9a58,#d9d4c8)}
.thumb-rug{background:radial-gradient(circle at 25% 20%,#4c92b8 0 8%,transparent 12%),linear-gradient(160deg,#a79378,#6f6252)}
.tags{padding:14px 6px;font-size:14px;line-height:18px;text-align:justify;text-align-last:center}
.ad{position:absolute;width:121px;height:97px;background:#fff;display:flex;align-items:center;justify-content:center;color:#111;font-size:20px}
</style>
</head>
<body>
<div class="abs brand"><span class="brand-mark"></span>Pebblopa</div>

<div class="panel" style="left:195px;top:62px;width:406px;height:69px"></div>
<div class="abs search-field"></div>
<div class="btn" style="left:418px;top:80px;width:104px">Search</div>

<div class="btn" style="left:614px;top:12px;width:104px">Log In</div>
<div class="btn" style="left:614px;top:64px;width:104px">Sign Up</div>
<div class="btn" style="left:614px;top:114px;width:104px">Store</div>
<div class="btn" style="left:614px;top:166px;width:104px">Parents</div>
<div class="btn" style="left:320px;top:166px;width:104px">Rules</div>

<nav>
<div class="btn" style="left:32px;top:216px;width:104px">Contests</div>
<div class="btn" style="left:148px;top:216px;width:104px">Videos</div>
<div class="btn" style="left:264px;top:216px;width:104px">Images</div>
<div class="btn" style="left:381px;top:216px;width:104px">Games</div>
<div class="btn" style="left:497px;top:216px;width:104px">Blogs</div>
<div class="btn" style="left:614px;top:216px;width:104px">UPLOAD</div>
</nav>

<div class="media" style="left:108px;top:278px;width:211px;height:158px;background:radial-gradient(ellipse at 55% 55%,#3b4a5a 0 18%,transparent 34%),linear-gradient(160deg,#4a362a,#1e1612)" role="img" aria-label="Announcement video still of a toy bird on a floor">
  <svg class="play" width="40" height="42" viewBox="0 0 40 42"><path d="M4 3 L37 21 L4 39 Z" fill="#f5b21a" stroke="#fff" stroke-width="3" stroke-linejoin="round"/></svg>
</div>

<div class="panel announce" style="left:418px;top:278px;width:301px;height:158px">
  <ul>
    <li><span class="bullet"></span>Text announcement</li>
    <li><span class="bullet"></span>Text announcement</li>
    <li><span class="bullet"></span>Text announcement</li>
    <li><span class="bullet"></span>Text announcement</li>
  </ul>
  <div class="scroll"><span></span></div>
</div>

<div class="panel" style="left:73px;top:481px;width:298px;height:235px">
  <ul class="cat-list">
    <li><span>Animations</span><span>3885 videos</span></li>
    <li><span>Contest Videos</span><span>112 videos</span></li>
    <li><span>Educational</span><span>914 videos</span></li>
    <li><span>General Videos</span><span>21,145 videos</span></li>
    <li><span>Pebblopa Announcer</span><span>11 videos</span></li>
    <li><span>Pebblopa Shows</span><span>2867 videos</span></li>
    <li><span>Music</span><span>3602 videos</span></li>
    <li><span>Online Safety</span><span>210 videos</span></li>
    <li><span>Pets and Animals</span><span>1141 videos</span></li>
  </ul>
</div>
<div class="btn" style="left:140px;top:462px;width:158px">Categories</div>

<div class="media" style="left:446px;top:500px;width:273px;height:204px;background:linear-gradient(180deg,#9dbbd0 0%,#8fbfa4 55%,#4f9a66 100%)" role="img" aria-label="Cartoon show title card over a city skyline">
  <svg class="play" width="40" height="42" viewBox="0 0 40 42"><path d="M4 3 L37 21 L4 39 Z" fill="#f5b21a" stroke="#fff" stroke-width="3" stroke-linejoin="round"/></svg>
</div>

<div class="panel" style="left:31px;top:747px;width:367px;height:419px"></div>
<div class="btn" style="left:134px;top:729px;width:160px">Featured Videos</div>
<div class="thumb thumb-girl" style="left:58px;top:783px" role="img" aria-label="Video thumbnail: girl with headphones"></div>
<div class="thumb thumb-title" style="left:174px;top:783px" role="img" aria-label="Video thumbnail: cartoon title card"></div>
<div class="thumb thumb-girl" style="left:290px;top:783px" role="img" aria-label="Video thumbnail: girl with headphones"></div>
<div class="thumb thumb-pet" style="left:58px;top:876px" role="img" aria-label="Video thumbnail: pet hamster"></div>
<div class="thumb thumb-boy" style="left:174px;top:876px" role="img" aria-label="Video thumbnail: boy talking"></div>
<div class="thumb thumb-pet" style="left:290px;top:876px" role="img" aria-label="Video thumbnail: pet hamster"></div>
<div class="thumb thumb-title" style="left:58px;top:968px" role="img" aria-label="Video thumbnail: cartoon title card"></div>
<div class="thumb thumb-rug" style="left:174px;top:968px" role="img" aria-label="Video thumbnail: marbles on a rug"></div>
<div class="thumb thumb-boy" style="left:290px;top:968px" role="img" aria-label="Video thumbnail: boy talking"></div>
<div class="thumb thumb-rug" style="left:58px;top:1060px" role="img" aria-label="Video thumbnail: marbles on a rug"></div>
<div class="thumb thumb-girl" style="left:174px;top:1060px" role="img" aria-label="Video thumbnail: girl with headphones"></div>
<div class="thumb thumb-title" style="left:290px;top:1060px" role="img" aria-label="Video thumbnail: cartoon title card"></div>

<div class="panel tags" style="left:434px;top:772px;width:285px;height:174px">
MARLOWE MARLOWE cute cute cute cute hot hot hot kids kids kids kids Brixo Brixo Brixo Brixo sarah sarah amazing amazing amazing amazing amazing amazing soccer soccer soccer soccer soccer brother brother brother brother brother brother brother second second second
</div>
<div class="btn" style="left:499px;top:750px;width:160px">Recent Tags</div>

<div class="ad" style="left:433px;top:1048px">Riffhouse</div>
<div class="ad" style="left:598px;top:1048px">Riffhouse</div>
</body>
</html>
```